Webdesign Handwerkerportal
Zielgruppe
Wir bieten eine Informationsplattform für Handwerkerbetriebe an.
Aufgabenstellung
wir benötigen ein Webdesign für unsere Werbsite.
Es handelt sich um eine Informationsplattform für Handwerker jeder Branche. Hier können ausschließlich registrierte Firmen und Handwerker Informationen austauschen.
Eine Menüleiste kann links oder am oberen Rand angebracht werden.
Das Design muss Seriösität vermitteln.
Kenntniss und Verständnis für Handwerker und deren Bedürfnisse sollte als Aussage im Design wie auch Vertrauen vermittelt werden.
z. B. 1 Auto / Pritsche, einen Kurvano einen Handwerker im Blaumann, einen Vorarbeiter im grauen Kittel, evtl. mit Helm. Für andere Vorschläge sind wir offen.
in diese Richtung ( ähnlich dem alten Zelvo Handshake, welcher aufeinanderzugehen und Vertrautheit vermittelt ) könnten wir uns vorstellen.

```html
<!DOCTYPE html>
<html lang="de">
<head>
<meta charset="utf-8">
<title>Meisterforum – Portal rund ums Handwerk</title>
<link href="https://fonts.googleapis.com/css2?family=Arimo:wght@400;700&display=swap" rel="stylesheet">
<style>
:root{
  --bar-dark:#3a3a3a;
  --page-grey:#f0f0f0;
  --text:#333;
  --blue:#2f62c0;
  --blue-light:#3ba3e8;
  --line:#555;
  --white:#fff;
}
*{box-sizing:border-box;margin:0;padding:0}
html,body{width:1107px;height:1200px;overflow:hidden}
body{position:relative;background:var(--white);font-family:"Arimo",Arial,sans-serif;color:var(--text)}
.abs{position:absolute}

.topbar{left:0;top:0;width:1107px;height:22px;background:var(--bar-dark)}
.topbar-links{right:125px;top:5px;font-size:10px;color:#eee;letter-spacing:.1px}
.topbar-links span{margin:0 4px}

.header{left:0;top:22px;width:1107px;height:113px;background:var(--page-grey)}
.header-fade{left:0;top:135px;width:1107px;height:55px;background:linear-gradient(#e2e2e2,#fff)}

.brand{left:260px;top:40px}
.brand-name{font-size:30px;font-weight:700;color:#3a3a3a;display:flex;align-items:center;gap:8px;line-height:1.1}
.brand-mark{width:14px;height:14px;background:var(--blue)}
.brand-tag{font-size:12px;font-weight:700;color:#3a3a3a;margin:3px 0 0 22px}

.login-label{left:557px;top:37px;font-size:11px;font-weight:700;color:#222}
.field{height:21px;border:1px solid #888;border-radius:3px;background:var(--white);font-size:11px;color:#999;padding:3px 8px}
.field-user{left:554px;top:53px;width:212px}
.field-pass{left:774px;top:53px;width:211px}
.go{width:25px;height:21px;background:linear-gradient(#4a8ee6,#2865c8);border-radius:0 3px 3px 0;display:flex;align-items:center;justify-content:center}
.go-pass{left:960px;top:53px}

.frame{left:101px;top:102px;width:905px;height:880px;border:1px solid var(--line);border-top:none;background:var(--white)}
.nav{left:101px;top:102px;width:905px;height:33px;background:linear-gradient(#5d5d5d,#2d2d2d);border-radius:5px 5px 0 0}
.search{left:363px;top:109px;width:186px;height:19px;background:#f6f3f3;border-radius:3px 0 0 3px;font-size:11px;color:#999;padding:3px 9px}
.go-search{left:548px;top:109px;height:19px;width:24px}
.nav-links{right:123px;top:112px;display:flex;gap:17px;font-size:11.5px;font-weight:700;color:#fff;letter-spacing:-.2px}

.hero{left:102px;top:135px;width:903px;height:199px;background:linear-gradient(90deg,#e9e9e9 0%,#f3f3f3 40%,#dcdcdc 100%);border-bottom:1px solid #ccc}
.hero-photo{left:530px;top:135px;width:475px;height:199px;background:linear-gradient(100deg,#efefef 0%,#d8d4cd 35%,#9aa3b5 70%,#cfd2d6 100%)}
.figure-photo{left:110px;top:24px;width:140px;height:310px;background:linear-gradient(#d9dde4,#8fa2c4)}
.hero-title{left:332px;top:190px;line-height:1}
.hero-title .l1{font-size:29px;color:#333}
.hero-title .l1 b{font-size:35px}
.hero-title .l2{font-size:42px;font-weight:700;color:var(--blue);margin:3px 0 0 12px;letter-spacing:.3px}

.feature{top:376px;width:265px}
.feature-icon{position:absolute;left:0;top:0;width:33px;height:33px;border-radius:6px;background:var(--blue);display:flex;align-items:center;justify-content:center}
.feature-body{margin-left:50px;width:194px}
.feature h3{font-size:13px;font-weight:700;color:#222;letter-spacing:.3px}
.feature p{font-size:11px;line-height:15px;color:#222;text-align:justify;margin-top:13px}
.feature a{font-size:11px;font-weight:700;color:var(--blue);text-decoration:none}

.quote-band{left:102px;top:510px;width:903px;height:166px;background:var(--page-grey)}
.section-title{left:102px;width:903px;text-align:center;font-size:37px;font-weight:400;color:#333;letter-spacing:-.3px}
.quote{left:144px;top:587px;width:841px;font-size:10.5px;line-height:16.5px;color:#333;letter-spacing:-.15px}
.qmark{font-size:30px;font-weight:700;color:var(--blue);font-family:Georgia,serif;line-height:1}

.card{top:776px;width:245px;height:163px}
.card-photo{height:138px;background:linear-gradient(110deg,#e8e4de 0%,#cdc6bb 40%,#8f9ab0 70%,#d3ccc0 100%)}
.card-caption{height:25px;background:var(--blue-light);color:#fff;font-size:11px;display:flex;align-items:center;justify-content:space-between;padding:0 10px 0 8px}

.footer{left:0;top:1021px;width:1107px;height:179px;background:var(--page-grey)}
.footer-links{left:0;top:1040px;width:1107px;text-align:center;font-size:11px;color:#333}
.footer-links span{margin:0 6px}
.social{left:0;top:1077px;width:1107px;display:flex;justify-content:center;gap:14px}
.social-item{display:flex;align-items:center;gap:5px;font-size:11px;color:#2a4f92;font-weight:700}
.social-item i{display:block;width:33px;height:33px;background:#2a58a8}
.footer-text{left:100px;top:1130px;width:907px;text-align:center;font-size:11px;line-height:16.5px;color:#333}
</style>
</head>
<body>
<div class="abs topbar"></div>
<div class="abs topbar-links">Mein Konto<span>|</span>Registrieren<span>|</span> Login<span>|</span>Logout</div>

<div class="abs header"></div>
<div class="abs header-fade"></div>

<div class="abs login-label">Login:</div>
<div class="abs field field-user">Benutzername</div>
<div class="abs field field-pass">Passwort</div>
<div class="abs go go-pass"><svg width="8" height="8" viewBox="0 0 8 8"><path d="M2 1l3 3-3 3" stroke="#fff" stroke-width="1.5" fill="none"/></svg></div>

<div class="abs frame"></div>
<div class="abs nav"></div>
<div class="abs search">Suche</div>
<div class="abs go go-search"><svg width="8" height="8" viewBox="0 0 8 8"><path d="M2 1l3 3-3 3" stroke="#fff" stroke-width="1.5" fill="none"/></svg></div>
<nav class="abs nav-links"><span>START</span><span>WIR ÜBER UNS</span><span>FAQ</span><span>IMPRESSUM</span><span>KONTAKT</span></nav>

<div class="abs hero"></div>
<div class="abs hero-photo" role="img" aria-label="Foto: Handwerker mit gelbem Helm misst auf einer Baustelle"></div>
<div class="abs figure-photo" role="img" aria-label="Foto: lächelnder Handwerker im blauen Hemd mit Werkzeuggürtel"></div>

<div class="abs brand">
  <div class="brand-name"><span class="brand-mark"></span>Meisterforum</div>
  <div class="brand-tag">Portal rund ums Handwerk</div>
</div>

<div class="abs hero-title">
  <div class="l1">Das <b>Portal</b> für</div>
  <div class="l2">Handwerker</div>
</div>

<section class="abs feature" style="left:122px">
  <div class="feature-icon"><svg width="18" height="20" viewBox="0 0 18 20"><rect x="2" y="2" width="14" height="17" rx="1" fill="none" stroke="#fff" stroke-width="1.6"/><rect x="6" y="0.5" width="6" height="3" fill="#fff"/><path d="M5 8h8M5 11h8M5 14h8" stroke="#fff" stroke-width="1.3"/></svg></div>
  <div class="feature-body"><h3>Lorem ipsum dolor sit</h3><p>Aenean commodo ligula eget dolor. Aenean massa. Cum sociis natoque penatibus et magnis dis parturient montes, nascetur ridiculus</p><a href="#">Mehr</a></div>
</section>
<section class="abs feature" style="left:426px">
  <div class="feature-icon"><svg width="22" height="18" viewBox="0 0 22 18"><circle cx="13" cy="5" r="4" fill="#fff"/><path d="M5 18c0-6 3-8 8-8s8 2 8 8z" fill="#fff"/><circle cx="7" cy="6" r="3" fill="#fff"/><path d="M1 16c0-4 2-6 5-6" stroke="#fff" stroke-width="2" fill="none"/></svg></div>
  <div class="feature-body"><h3>Lorem ipsum dolor sit</h3><p>Aenean commodo ligula eget dolor. Aenean massa. Cum sociis natoque penatibus et magnis dis parturient montes, nascetur ridiculus</p><a href="#">Mehr</a></div>
</section>
<section class="abs feature" style="left:740px">
  <div class="feature-icon"><svg width="16" height="22" viewBox="0 0 16 22"><path d="M8 1a7 7 0 0 0-4 12.7V16h8v-2.3A7 7 0 0 0 8 1z" fill="none" stroke="#fff" stroke-width="1.8"/><path d="M4.5 18.5h7M5.5 21h5" stroke="#fff" stroke-width="1.6"/></svg></div>
  <div class="feature-body"><h3>Lorem ipsum dolor sit</h3><p>Aenean commodo ligula eget dolor. Aenean massa. Cum sociis natoque penatibus et magnis dis parturient montes, nascetur ridiculus</p><a href="#">Mehr</a></div>
</section>

<div class="abs quote-band"></div>
<h2 class="abs section-title" style="top:528px">Integer tincidunt</h2>
<div class="abs qmark" style="left:123px;top:584px">”</div>
<p class="abs quote">Vivamus elementum semper nisi. Aenean vulputate eleifend tellus. Aenean leo ligula, porttitor eu, consequat vitae, eleifend ac, enim. Aliquam lorem ante, dapibus in, viverra quis, feugiat a, tellus. Phasellus viverra nulla ut metus varius laoreet. Quisque rutrum. Aenean imperdiet. Etiam ultricies nisi vel augue. Curabitur ullamcorper ultricies nisi. Nam eget dui. Etiam rhoncus. Maecenas tempus, tellus eget condimentum rhoncus, sem quam semper libero, sit amet adipiscing sem neque sed <span class="qmark" style="font-size:26px;vertical-align:-10px">”</span></p>

<h2 class="abs section-title" style="top:712px">Maecenas nec odio et ante tincidunt tempus</h2>

<article class="abs card" style="left:123px"><div class="card-photo" role="img" aria-label="Foto: Handwerker mit Helm bei der Arbeit"></div><div class="card-caption"><span>ellus. Phasellus viverra nulla</span><svg width="7" height="8" viewBox="0 0 7 8"><path d="M2 1l3 3-3 3" stroke="#fff" stroke-width="1.4" fill="none"/></svg></div></article>
<article class="abs card" style="left:427px"><div class="card-photo" role="img" aria-label="Foto: Handwerker mit Helm bei der Arbeit"></div><div class="card-caption"><span>ellus. Phasellus viverra nulla</span><svg width="7" height="8" viewBox="0 0 7 8"><path d="M2 1l3 3-3 3" stroke="#fff" stroke-width="1.4" fill="none"/></svg></div></article>
<article class="abs card" style="left:740px"><div class="card-photo" role="img" aria-label="Foto: Handwerker mit Helm bei der Arbeit"></div><div class="card-caption"><span>ellus. Phasellus viverra nulla</span><svg width="7" height="8" viewBox="0 0 7 8"><path d="M2 1l3 3-3 3" stroke="#fff" stroke-width="1.4" fill="none"/></svg></div></article>

<footer>
  <div class="abs footer"></div>
  <div class="abs footer-links">Start<span>|</span>Wir über uns<span>|</span>FAQ<span>|</span>Impressum<span>|</span>Kontakt</div>
  <div class="abs social">
    <div class="social-item"><i></i>Freundnetz</div>
    <div class="social-item"><i></i>Zwitscher</div>
    <div class="social-item"><i></i>Kreisnetz</div>
  </div>
  <p class="abs footer-text">Curabitur ullamcorper ultricies nisi. Nam eget dui. Etiam rhoncus. Maecenas tempus, tellus eget condimentum rhoncus, sem quam semper libero, sit amet adipiscing sem neque sed ipsum. Nam quam nunc, blandit vel, luctus pulvinar, hendrerit id, lorem. Maecenas nec odio et ante tincidunt tempus. Donec</p>
</footer>
</body>
</html>
```